Briney Lark Fare landing page design

We need a landing page designed for an ecommerce website that sales fresh US domestic shrimp from the Gulf of Mexico and ships them direct to the consumer "From Our Shore To Your Door". For the landing page, we would like customers to be able to place an order and or inquire further about our product as well as links to social media. The company logo is attached

1 page

```html
<!DOCTYPE html>
<html lang="en">
<head>
<meta charset="utf-8">
<title>Briney Lark Fare</title>
<link href="https://fonts.googleapis.com/css2?family=Roboto:wght@300;400;500;700&display=swap" rel="stylesheet">
<style>
:root{
  --navy:#2c3e50;
  --navy-line:#3a4d61;
  --green:#7cad3c;
  --green-dark:#4b7d1f;
  --teal:#1fc8a8;
  --ink:#2f3a45;
  --muted:#8a9096;
  --white:#ffffff;
}
*{box-sizing:border-box;margin:0;padding:0}
html,body{width:1200px;height:1200px;overflow:hidden;background:#fff;font-family:'Roboto',sans-serif;color:var(--ink)}
.stage{position:absolute;left:216px;top:0;width:960px;height:1500px;transform:scale(0.8);transform-origin:0 0}
.abs{position:absolute}
.topbar{left:0;top:0;width:960px;height:30px;background:var(--navy);color:#e6ebef;font-size:9px}
.topbar span{position:absolute;top:10px}
.topbar .reg{color:var(--teal)}
.dot{position:absolute;width:12px;height:12px;border-radius:50%;background:#e6ebef}
.topbar .sep{position:absolute;top:0;width:1px;height:30px;background:var(--navy-line)}
.header{left:0;top:30px;width:960px;height:96px;background:#fff}
.logo-mark{left:123px;top:8px;width:74px;height:74px;border-radius:50%;border:2px solid #9bb3c4}
.logo-name{left:205px;top:32px;font-size:24px;font-weight:400;letter-spacing:3px;color:#3d4650}
.nav a{position:absolute;top:42px;font-size:9px;color:var(--ink);text-decoration:none;letter-spacing:.3px}
.nav .active{color:var(--green)}
.nav .big{font-size:10.5px;font-weight:500;top:41px}
.hero{left:0;top:126px;width:960px;height:430px;background:
  radial-gradient(ellipse at 45% 60%,#f2826a 0%,#ec7a62 35%,rgba(240,150,130,.6) 60%,rgba(240,240,240,0) 80%),
  linear-gradient(180deg,#d9dadc 0%,#f0f0ef 60%,#e9e7e4 100%)}
.arrow{top:131px;width:48px;height:48px}
.arrow.prev{left:28px;background:rgba(255,255,255,.35)}
.arrow.next{left:889px;background:var(--green-dark)}
.orderbar{left:0;top:556px;width:960px;height:63px;background:var(--navy);color:#b6c0c9;font-size:12px}
.orderbar .ttl{position:absolute;left:150px;top:23px;color:#fff;font-size:13px;font-weight:500}
.orderbar .ttl b{font-weight:300}
.orderbar label{position:absolute;top:26px}
.field{position:absolute;top:18px;height:28px;background:#fff;color:#5a636b;font-size:12px;padding:7px 6px}
.field i{position:absolute;right:6px;top:8px;width:12px;height:12px;border:1px solid #a8adb2;border-radius:2px}
.field i.round{border-radius:50%;background:#b8bdc2;border:none}
.btn{position:absolute;left:764px;top:17px;width:65px;height:30px;background:var(--green);color:#fff;font-size:12px;text-align:center;line-height:30px}
.offers-bg{left:0;top:658px;width:960px;height:585px;background:
  radial-gradient(ellipse at 20% 25%,rgba(250,225,190,.8),rgba(255,255,255,0) 45%),
  radial-gradient(ellipse at 85% 75%,rgba(252,236,200,.9),rgba(255,255,255,0) 50%),
  radial-gradient(ellipse at 15% 80%,rgba(250,215,180,.7),rgba(255,255,255,0) 45%),
  linear-gradient(180deg,#fdf9ee,#fffdf6 50%,#fcf6e6)}
.h2{width:960px;left:0;text-align:center;font-size:18px;font-weight:500;color:var(--navy)}
.sub{width:960px;left:0;text-align:center;font-size:9.5px;color:#4a525a}
.card{position:absolute;top:803px;height:149px;background:#f3f3f1;box-shadow:0 1px 3px rgba(0,0,0,.08)}
.card .img{position:absolute;left:5px;top:2px;right:5px;height:113px}
.card .cap{position:absolute;left:7px;top:120px;font-size:8.5px;color:#555;line-height:10px}
.card .cap small{font-size:7.5px}
.card .chev{position:absolute;right:12px;top:126px}
.card.hot{top:785px;height:178px;border:2px solid var(--teal);background:var(--navy)}
.card.hot .img{left:0;right:0;top:0;height:131px}
.card.hot .cap{top:138px;color:#fff}
.card.hot .chev{top:144px}
.quote{position:absolute;background:rgba(255,255,255,.85);border:1px solid #e3e3e3;font-size:9px;line-height:13px;padding:14px 16px;color:#2f3a45}
.quote .who{color:var(--teal);font-size:11px;margin-top:2px}
.quote.faded{opacity:.45;background:rgba(255,255,255,.5)}
.footer{left:0;top:1243px;width:960px;height:257px;background:var(--navy);color:#fff}
.footer h3{position:absolute;top:35px;font-size:15px;font-weight:400;color:var(--teal)}
.footer .txt{position:absolute;font-size:9px;line-height:12.5px}
.sub-in{position:absolute;left:136px;top:105px;width:88px;height:19px;background:#fff;color:#888;font-size:7px;padding:5px}
.go{position:absolute;left:229px;top:105px;width:28px;height:19px;background:var(--teal);font-size:8px;text-align:center;line-height:19px}
.about-box{position:absolute;left:295px;top:62px;width:142px;height:86px;border:1px solid #c7cfd6;padding:4px;font-size:9px;line-height:12px}
.tag{position:absolute;height:16px;border:1px solid #c7cfd6;font-size:7.5px;padding:3px 4px}
.rule{left:0;top:1417px;width:960px;height:1px;background:var(--navy-line)}
.copy{width:960px;left:0;text-align:center}
</style>
</head>
<body>
<div class="stage">

  <div class="abs topbar">
    <span style="left:135px">&#9679; Customer Login</span>
    <span style="left:230px">&#9633; Not a Member ? <em class="reg" style="font-style:normal">Register</em></span>
    <span style="left:360px">Call Us Now : 000-123-4567</span>
    <div class="sep" style="left:742px"></div>
    <div class="dot" style="left:748px;top:9px"></div>
    <div class="sep" style="left:768px"></div>
    <div class="dot" style="left:775px;top:9px"></div>
    <div class="sep" style="left:795px"></div>
    <div class="dot" style="left:802px;top:9px"></div>
    <div class="sep" style="left:822px"></div>
  </div>

  <header class="abs header">
    <div class="abs logo-mark"></div>
    <div class="abs logo-name">Briney Lark Fare</div>
    <nav class="nav">
      <a class="active" style="left:647px">HOME</a>
      <a class="big" style="left:695px">ORDER NOW</a>
      <a style="left:778px">ABOUT US</a>
    </nav>
  </header>

  <section class="abs hero" role="img" aria-label="Platter of fresh boiled Gulf shrimp with lemon and lime wedges and dill">
    <div class="abs arrow prev"></div>
    <div class="abs arrow next">
      <svg width="48" height="48" viewBox="0 0 48 48"><polyline points="20,15 29,24 20,33" fill="none" stroke="#fff" stroke-width="2"/></svg>
    </div>
  </section>

  <form class="abs orderbar">
    <div class="ttl">ORDER <b>NOW</b></div>
    <label style="left:256px">Where</label>
    <div class="field" style="left:296px;width:111px">distination<i class="round"></i></div>
    <label style="left:420px">When</label>
    <div class="field" style="left:460px;width:107px">select date<i></i></div>
    <label style="left:577px">Quantity</label>
    <div class="field" style="left:629px;width:102px"><i></i></div>
    <div class="btn">Order Now</div>
  </form>

  <section class="abs offers-bg" role="img" aria-label="Soft faded background photo of shrimp dishes"></section>

  <h2 class="abs h2" style="top:710px">SPECIAL OFFERS</h2>
  <p class="abs sub" style="top:742px">Best 2014 packages where people love to stay!</p>

  <div class="card" style="left:0;width:148px"><div class="img" role="img" aria-label="Grilled prawns and squid" style="background:linear-gradient(135deg,#c9673a,#f0a070 50%,#8a4a2e)"></div><div class="cap">shrimp<br><small>price: 9.9 $</small></div><svg class="chev" width="10" height="6"><polyline points="1,1 5,5 9,1" fill="none" stroke="#888"/></svg></div>
  <div class="card" style="left:158px;width:150px"><div class="img" role="img" aria-label="Roasted jumbo shrimp on greens" style="background:linear-gradient(135deg,#d66a2a,#f2a04c 50%,#b8c7a4)"></div><div class="cap">shrimp<br><small>price: 9.9 $</small></div><svg class="chev" width="10" height="6"><polyline points="1,1 5,5 9,1" fill="none" stroke="#888"/></svg></div>
  <div class="card hot" style="left:323px;width:151px"><div class="img" role="img" aria-label="Red shrimp with lemon wedge" style="background:linear-gradient(135deg,#e0433a,#f07060 50%,#f4e3b0)"></div><div class="cap">shrimp<br><small>price: 9.9 $</small></div><svg class="chev" width="10" height="6"><polyline points="1,1 5,5 9,1" fill="none" stroke="#fff" stroke-width="1.5"/></svg></div>
  <div class="card" style="left:488px;width:150px"><div class="img" role="img" aria-label="Single shrimp held by chopsticks on dark background" style="background:radial-gradient(circle at 45% 50%,#c46a28,#2a1a10 35%,#0a0a0a 70%)"></div><div class="cap">shrimp<br><small>price: 9.9 $</small></div><svg class="chev" width="10" height="6"><polyline points="1,1 5,5 9,1" fill="none" stroke="#333"/></svg></div>
  <div class="card" style="left:650px;width:150px"><div class="img" role="img" aria-label="Peeled cooked shrimp" style="background:linear-gradient(135deg,#f3a27e,#f8c9b0 50%,#e88a66)"></div><div class="cap">shrimp<br><small>price: 9.9 $</small></div><svg class="chev" width="10" height="6"><polyline points="1,1 5,5 9,1" fill="none" stroke="#333"/></svg></div>
  <div class="card" style="left:812px;width:148px"><div class="img" role="img" aria-label="Peeled cooked shrimp" style="background:linear-gradient(135deg,#f3a27e,#f8c9b0 50%,#e88a66)"></div><div class="cap">shrimp<br><small>price: 9.9 $</small></div><svg class="chev" width="10" height="6"><polyline points="1,1 5,5 9,1" fill="none" stroke="#333"/></svg></div>

  <h2 class="abs h2" style="top:1061px;font-size:15px;left:-12px">HAPPY CLIENTS</h2>
  <p class="abs sub" style="top:1085px;left:-12px">what customer say about us and why love our services!</p>

  <div class="quote faded" style="left:-40px;top:1120px;width:110px;height:85px;padding-left:40px">ting and typese stry's.</div>
  <div class="quote faded" style="left:45px;top:1120px;width:285px;height:85px;border-top:none">Lorem Ipsum is simply dummy text of the printing and typese ting industry. Lorem Ipsum has been the industry's.<div class="who">Client Name</div></div>
  <div class="quote" style="left:337px;top:1120px;width:284px;height:85px;border-top:3px solid var(--teal);padding-top:10px">Lorem Ipsum is simply dummy text of the printing and typeset industry. Lorem Ipsum has been the industry's standard dummy text ever hen an with new version look.<div class="who">Client Name</div></div>
  <div class="quote faded" style="left:632px;top:1120px;width:284px;height:85px;border-top:none;padding-top:10px">Lorem Ipsum is simply dummy text of the printing and typeset ting industry. Lorem Ipsum has been the industry's.<div class="who">Client Name</div></div>

  <footer class="abs footer">
    <h3 style="left:137px">Newsletter</h3>
    <p class="txt" style="left:137px;top:60px;width:135px">Lorem Ipsum is simply dummy text of the printing and typeset industry. Lorem Ipsum has</p>
    <div class="sub-in">Subscribes...</div>
    <div class="go">GO</div>

    <h3 style="left:295px">About Us</h3>
    <div class="about-box">Lorem Ipsum is simply dummy<br><span style="font-size:7.5px">images</span><br>Lorem Ipsum is simply dummy<br><span style="font-size:7.5px">images</span></div>

    <h3 style="left:487px">Tags</h3>
    <div class="tag" style="left:489px;top:60px;width:51px">text1</div>
    <div class="tag" style="left:544px;top:60px;width:70px">text1</div>
    <div class="tag" style="left:489px;top:81px;width:63px">text1</div>
    <div class="tag" style="left:556px;top:81px;width:35px">text1</div>
    <div class="tag" style="left:489px;top:101px;width:58px">text1</div>
    <div class="tag" style="left:550px;top:101px;width:41px">text1</div>
    <div class="tag" style="left:595px;top:101px;width:24px">text1</div>
    <div class="tag" style="left:489px;top:125px;width:58px">text1</div>
    <div class="tag" style="left:550px;top:125px;width:41px">text1</div>
    <div class="tag" style="left:595px;top:125px;width:24px">text1</div>

    <h3 style="left:664px;font-weight:700">Address</h3>
    <p class="txt" style="left:665px;top:58px;font-size:7.5px;line-height:15.5px">Company Name<br>address<br><span style="color:var(--teal)">E-mail:</span> orders@brineylark.example</p>
    <div class="dot" style="left:671px;top:115px;background:#fff"></div>
    <div class="dot" style="left:695px;top:115px;background:#fff"></div>
    <div class="dot" style="left:724px;top:115px;background:#fff"></div>
  </footer>

  <div class="abs rule"></div>
  <p class="abs copy" style="top:1436px;font-size:9px;color:var(--teal)">Comapny Name</p>
  <p class="abs copy" style="top:1453px;font-size:7.5px;color:#b6c0c9">Copyright @brineylark. All Right Reserved.</p>

</div>
</body>
</html>
```